Business Card Design Project

We are not a new company, but renamed to "Norvanta Kitchens" last year. We specialize in modern high-end cabinetry imports. We would like to communicate a sense of quality and cutting edge technology. Ideally the design would incorporate our logo colors, silver, red and preferably a black, matte background. Though we are open to suggestions.
Logo is attached.
Edit: I have attached rough drafts of the previous cards, this way you will have all necessary content that needs to go on the cards.
Reason: We have received a lot of great designs, but due to the sheer number we couldn't respond to all. We will extend the deadline for another 7 days to finalize and provide feedback to designers.
Thank you for your hard work!
Industry/Entity Type
Business
Look and feel
Each slider illustrates characteristics of the customer's brand and the style your logo design should communicate.

```html
<!DOCTYPE html>
<html lang="en">
<head>
<meta charset="utf-8">
<title>Norvanta Kitchens — Business Card</title>
<link rel="stylesheet" href="https://fonts.googleapis.com/css2?family=Michroma&family=Exo+2:wght@400;600&display=swap">
<style>
  :root {
    --backdrop: #8a8a8c;
    --card-black: #0b0b0c;
    --card-charcoal: #1c1d1f;
    --silver: #c9cacc;
    --silver-dim: #9c9ea1;
    --red: #e0262b;
    --text-light: #e6e6e6;
  }
  * { box-sizing: border-box; margin: 0; padding: 0; }
  html, body { width: 1200px; height: 840px; overflow: hidden; }
  body {
    background: var(--backdrop);
    display: flex;
    align-items: center;
    justify-content: center;
    gap: 60px;
    font-family: "Exo 2", sans-serif;
  }
  .card {
    width: 520px;
    height: 297px;
    position: relative;
    box-shadow: 0 18px 40px rgba(0,0,0,.35);
  }
  .card-front {
    background: linear-gradient(150deg, #1a1a1b 0%, var(--card-black) 55%, #050505 100%);
    display: flex;
    align-items: center;
    justify-content: center;
  }
  .brand {
    display: flex;
    align-items: center;
    gap: 12px;
    font-family: "Michroma", sans-serif;
    color: var(--silver);
    text-transform: uppercase;
    letter-spacing: 1px;
  }
  .brand-mark {
    background: var(--silver);
    flex: none;
  }
  .card-front .brand { font-size: 22px; }
  .card-front .brand-mark { width: 26px; height: 26px; }

  .card-back {
    background: linear-gradient(160deg, #26272a 0%, var(--card-charcoal) 45%, #101112 100%);
    color: var(--text-light);
  }
  .holder {
    position: absolute;
    right: 28px;
    top: 30px;
    text-align: right;
  }
  .holder-name {
    font-family: "Michroma", sans-serif;
    color: var(--red);
    font-size: 17px;
    letter-spacing: 2px;
    text-transform: uppercase;
  }
  .holder-title {
    font-family: "Michroma", sans-serif;
    font-size: 7px;
    letter-spacing: 1px;
    text-transform: uppercase;
    margin-top: 4px;
  }
  .rule {
    position: absolute;
    right: 0;
    height: 1px;
    background: var(--red);
  }
  .rule-top { top: 82px; width: 250px; }
  .rule-mid { top: 146px; width: 250px; }
  .address {
    position: absolute;
    left: 270px;
    top: 100px;
    font-size: 10.5px;
    line-height: 16px;
    letter-spacing: 1.2px;
    text-transform: uppercase;
  }
  .contacts {
    position: absolute;
    left: 270px;
    top: 160px;
    list-style: none;
    font-size: 10.5px;
    letter-spacing: 1.2px;
  }
  .contacts li {
    display: flex;
    align-items: center;
    gap: 10px;
    height: 19px;
  }
  .contacts svg { width: 13px; height: 13px; fill: var(--red); flex: none; }
  .contacts .email { font-size: 8.5px; text-transform: uppercase; }
  .card-back .brand {
    position: absolute;
    left: 28px;
    bottom: 30px;
    font-size: 13px;
    gap: 9px;
  }
  .card-back .brand-mark { width: 16px; height: 16px; }
</style>
</head>
<body>
  <section class="card card-front" aria-label="Card front">
    <div class="brand"><span class="brand-mark"></span><span class="brand-name">Norvanta Kitchens</span></div>
  </section>

  <section class="card card-back" aria-label="Card back">
    <div class="holder">
      <p class="holder-name">Marcus Verlin</p>
      <p class="holder-title">Director</p>
    </div>
    <div class="rule rule-top"></div>
    <p class="address">1820 - 64 St. Edmonton,<br>AB T5K 2P4</p>
    <div class="rule rule-mid"></div>
    <ul class="contacts">
      <li>
        <svg viewBox="0 0 16 16" aria-label="Phone"><path d="M2 5c0-2 2-3 3-3l1.5 3-1.5 1.5c.8 1.8 2.2 3.2 4 4L10.5 9l3 1.5c0 1-1 3-3 3C6 13.5 2 9.5 2 5z"/></svg>
        <span>780.555.0142</span>
      </li>
      <li>
        <svg viewBox="0 0 16 16" aria-label="Mobile"><path d="M4.5 1h7v14h-7zM6 3v9h4V3zm1.5 10.2h1v1h-1z" fill-rule="evenodd"/></svg>
        <span>780.555.0178</span>
      </li>
      <li>
        <svg viewBox="0 0 16 16" aria-label="Fax"><path d="M4 1h6l2 2v3H4zM1.5 7h13v6h-2.5v2h-8v-2H1.5zM5.5 11v3h5v-3z" fill-rule="evenodd"/></svg>
        <span>780.555.0193</span>
      </li>
      <li>
        <svg viewBox="0 0 16 16" aria-label="Email"><path d="M1 3.5h14v9H1zm1.5 1.2v.3L8 9l5.5-4v-.3zM2.5 6.6v4.4h11V6.6L8 10.6z" fill-rule="evenodd"/></svg>
        <span class="email">marcus@norvantakitchens.ca</span>
      </li>
    </ul>
    <div class="brand"><span class="brand-mark"></span><span class="brand-name">Norvanta Kitchens</span></div>
  </section>
</body>
</html>
```